Video blogger website.

I'm looking to build a video blogger website I want cool, unique design. The ability to add banners on top of page. I would like to use embedded videos from sources like ClipVerra etc with the ability to share on social media . If needed I can provide example sites upon request. Like / dislike button similar to ClipVerra and Video View counter .10-15 pages with the availability to add more pages as site grows. I want the overall outline of the site to be original, but I want banners and all functions all to be done in WordPress. But I don't want a completely WordPress website due to certain limitations. Please no cookie cutters!!

Target Market(s)

Music, Comedy teens to adults

Build

Coding

Coded - Design and coding required

Number of Pages Required

5+ page

Colors

Designer to choose colors to be used in the design.

Requirements
Should not have
• No log in

```html
<!DOCTYPE html>
<html lang="en">
<head>
<meta charset="utf-8">
<title>Kove Clips</title>
<link href="https://fonts.googleapis.com/css2?family=Oswald:wght@400;500&family=Open+Sans:wght@400;600;700&family=Roboto:wght@400;500;700&display=swap" rel="stylesheet">
<style>
:root{
  --red:#e81f30;
  --ink:#222;
  --text:#4a4a4a;
  --muted:#777;
  --rule:#e3e3e3;
  --field:#f5f5f5;
  --grey:#9a9a9a;
  --footer:#262626;
  --white:#fff;
}
*{box-sizing:border-box;margin:0;padding:0}
html,body{width:1200px;height:2804px;overflow:hidden;background:var(--white)}
body{position:relative;font-family:'Roboto',sans-serif;color:var(--ink)}
a{color:inherit;text-decoration:none}

/* header */
.site-header{position:absolute;left:0;top:0;width:1200px;height:125px}
.brand{position:absolute;left:99px;top:48px;display:flex;align-items:center;gap:10px;color:var(--red);font:700 25px 'Roboto',sans-serif;letter-spacing:.5px}
.brand-mark{width:36px;height:30px;background:var(--red);border-radius:4px}
.search{position:absolute;left:855px;top:24px;display:flex;gap:7px}
.search-field{width:157px;height:34px;border:1px solid #ddd;border-radius:3px}
.search-btn{width:82px;height:34px;background:#7f7f7f;color:var(--white);border-radius:3px;font:500 14px 'Roboto',sans-serif;display:flex;align-items:center;justify-content:center}
.main-nav{position:absolute;top:84px;left:0;width:1200px;height:24px;font:400 16px 'Open Sans',sans-serif;color:#222}
.main-nav a{position:absolute;transform:translateX(-50%);white-space:nowrap}

/* hero */
.hero{position:absolute;left:0;top:125px;width:1200px;height:558px}
.hero-photo{position:absolute;inset:0;clip-path:polygon(0 0,100% 0,100% 507px,50% 558px,0 507px);
  background:linear-gradient(180deg,#2d4a66 0%,#4d6d85 35%,#5f8a95 55%,#2f5a62 75%,#24403f 100%)}
.hero-photo::after{content:"";position:absolute;inset:0;background:radial-gradient(ellipse at 85% 30%,rgba(20,45,25,.8),transparent 55%)}
.hero-content{position:absolute;left:0;top:0;width:1200px;text-align:center;color:var(--white)}
.hero-title{position:absolute;top:118px;width:100%;font:700 51px 'Open Sans',sans-serif;letter-spacing:1px}
.hero-lead{position:absolute;top:200px;left:200px;width:800px;font:400 14px/24px 'Open Sans',sans-serif}
.hero-btn{position:absolute;left:535px;top:298px;width:131px;height:52px;border:2px solid var(--white);font:600 15px 'Open Sans',sans-serif;display:flex;align-items:center;justify-content:center}
.hero-dots{position:absolute;top:393px;left:546px;display:flex;gap:7px}
.hero-dots span{width:15px;height:15px;border:2px solid var(--white);border-radius:50%}
.hero-dots span.active{background:var(--red);border-color:var(--white)}

/* section headings */
.section-title{font:400 27px 'Oswald',sans-serif;color:var(--red)}

/* latest */
.latest{position:absolute;left:99px;top:728px;width:739px}
.latest-head{height:52px;border-bottom:2px solid var(--rule);position:relative}
.latest-head .section-title{position:absolute;left:0;top:0}
.more-btn{position:absolute;right:0;top:3px;width:86px;height:36px;background:var(--red);color:var(--white);font:500 14px 'Roboto',sans-serif;display:flex;align-items:center;justify-content:center}

.post{margin-top:32px}
.post-media{height:312px;border:1px solid #ddd;padding:4px;position:relative}
.post-photo{width:100%;height:100%}
.photo-friends{background:linear-gradient(120deg,#a8b6c4 0%,#7d7a78 40%,#5f6e8a 70%,#c7b8a6 100%)}
.photo-camp{background:linear-gradient(180deg,#6f7a78 0%,#b7884a 45%,#6c5230 75%,#3a3124 100%)}
.play{position:absolute;left:50%;top:50%;transform:translate(-50%,-50%)}
.post-head{margin-top:22px;display:flex;justify-content:space-between;align-items:center;height:26px}
.post-title{font:500 19px 'Roboto',sans-serif;color:var(--red)}
.post-date{font:italic 400 13px 'Open Sans',sans-serif;color:var(--red);display:flex;align-items:center;gap:5px}
.post-body{margin-top:12px;font:400 14px/24px 'Open Sans',sans-serif;color:var(--text);text-align:justify}
.post-actions{margin-top:22px;height:49px;display:flex;align-items:center}
.read-btn{width:165px;height:49px;background:var(--red);color:var(--white);font:500 16px 'Roboto',sans-serif;display:flex;align-items:center;justify-content:center}
.stat{display:flex;align-items:center;gap:9px;font:500 16px 'Roboto',sans-serif;color:#333;margin-left:36px}
.share{margin-left:auto;display:flex;gap:4px}
.share span{width:27px;height:27px;border:1.5px solid #999;border-radius:50%}
.post-rule{margin-top:35px;border-top:2px solid var(--rule)}
.comment-label{margin-top:26px;font:500 16px 'Roboto',sans-serif;color:#333}
.comment-field{margin-top:16px;height:90px;background:var(--field);border:1px solid #ddd;border-radius:3px;padding:12px;font:400 12px 'Open Sans',sans-serif;color:#666}
.post-end{margin-top:34px;border-top:2px solid var(--rule)}

.pager{margin-top:30px;display:flex;gap:5px;height:34px}
.pager a{background:var(--grey);color:var(--white);font:700 15px 'Roboto',sans-serif;display:flex;align-items:center;justify-content:center;min-width:38px;padding:0 10px}
.pager a.current,.pager a.prev{background:var(--red)}
.pager a.next{width:92px}

/* sidebar */
.upnext{position:absolute;left:877px;top:744px;width:224px}
.upnext-head{text-align:center}
.upnext-head .section-title{font-size:25px}
.upnext-head::after{content:"";display:block;width:74px;height:2px;background:var(--red);margin:8px auto 0}
.clip{margin-top:33px}
.clip + .clip{margin-top:38px}
.clip-media{height:161px;border:1px solid #ddd;position:relative}
.clip-photo{width:100%;height:100%}
.clip-1{background:linear-gradient(160deg,#4a4a2e,#6e6a3e 50%,#2e3320)}
.clip-2{background:linear-gradient(160deg,#c9c1b7,#8a7a6e 50%,#3f4a5e)}
.clip-3{background:linear-gradient(160deg,#5f6d4c,#e8e6e2 50%,#9aa39a)}
.clip-4{background:linear-gradient(180deg,#dfe3e6,#b3a98a 45%,#7a8e5c 60%,#a0785a)}
.clip-5{background:linear-gradient(160deg,#d8b880,#9a6e3a 50%,#4a5a2a)}
.clip .play svg{width:44px;height:44px}
.clip-text{margin-top:14px;font:400 11.5px/16px 'Open Sans',sans-serif;color:#333;text-align:justify}
.clip-meta{margin-top:16px;display:flex;align-items:center;gap:14px;font:500 10px 'Roboto',sans-serif;color:#222;padding-bottom:12px;border-bottom:2px solid var(--rule)}
.clip-meta .m{display:flex;align-items:center;gap:4px}
.clip-meta .share span{width:15px;height:15px;border-width:1px}

/* footer */
.site-footer{position:absolute;left:0;top:2480px;width:1200px;height:324px;background:var(--footer);color:var(--white)}
.footer-brand{position:absolute;top:87px;left:0;width:100%;display:flex;justify-content:center;align-items:center;gap:12px;font:500 29px 'Roboto',sans-serif;letter-spacing:.5px}
.footer-brand .brand-mark{background:var(--white);width:44px;height:36px}
.footer-nav{position:absolute;top:189px;left:0;width:100%;display:flex;justify-content:center;font:500 16px 'Roboto',sans-serif}
.footer-nav span.sep{margin:0 24px}
.footer-rule{position:absolute;top:240px;left:99px;width:1002px;border-top:1px solid #bdbdbd}
.copyright{position:absolute;top:271px;left:99px;font:500 14px 'Roboto',sans-serif}
.footer-social{position:absolute;top:263px;right:99px;display:flex;gap:6px}
.footer-social span{width:33px;height:33px;border:2px solid var(--white);border-radius:50%}
</style>
</head>
<body>

<header class="site-header">
  <a class="brand" href="#"><span class="brand-mark"></span>KOVE CLIPS</a>
  <div class="search"><div class="search-field"></div><div class="search-btn">Search</div></div>
  <nav class="main-nav">
    <a href="#" style="left:497px">Home</a>
    <a href="#" style="left:595px">About</a>
    <a href="#" style="left:726px">Upload Videos</a>
    <a href="#" style="left:858px">Contact</a>
    <a href="#" style="left:961px">News</a>
    <a href="#" style="left:1068px">Portfolio</a>
  </nav>
</header>

<section class="hero">
  <div class="hero-photo" role="img" aria-label="Tropical sea with long-tail boats and palm leaves"></div>
  <div class="hero-content">
    <h1 class="hero-title">KOVE CLIPS</h1>
    <p class="hero-lead">Duis aute irure dolor in reprehenderit in voluptate velit esse cillum dolore eu fugiat nulla pariatur. Excepteur sint occaecat cupidatat non proident.</p>
    <a class="hero-btn" href="#">READ MORE</a>
    <div class="hero-dots"><span class="active"></span><span></span><span></span><span></span><span></span></div>
  </div>
</section>

<main class="latest">
  <div class="latest-head">
    <h2 class="section-title">Latest Videos</h2>
    <a class="more-btn" href="#">MORE</a>
  </div>

  <article class="post">
    <div class="post-media">
      <div class="post-photo photo-friends" role="img" aria-label="Group of friends looking at a tablet outdoors"></div>
      <div class="play"><svg width="70" height="70" viewBox="0 0 70 70"><circle cx="35" cy="35" r="32" fill="rgba(0,0,0,.25)" stroke="#fff" stroke-width="4"/><path d="M28 22 L50 35 L28 48 Z" fill="#fff"/></svg></div>
    </div>
    <div class="post-head">
      <h3 class="post-title">Nemo enim ipsam voluptatem quia voluptas</h3>
      <span class="post-date"><svg width="12" height="12" viewBox="0 0 12 12"><rect x="1" y="2" width="10" height="9" fill="none" stroke="#e81f30" stroke-width="1.4"/><path d="M1 5h10M4 0.5v3M8 0.5v3" stroke="#e81f30" stroke-width="1.4"/></svg>January 21, 2017</span>
    </div>
    <p class="post-body">Sed ut perspiciatis unde omnis iste natus error sit voluptatem accusantium doloremque laudantium, totam rem aperiam, eaque ipsa quae ab illo inventore veritatis et quasi architecto beatae vitae dicta sunt explicabo. Nemo enim ipsam voluptatem quia voluptas sit aspernatur aut odit aut fugit.</p>
    <div class="post-actions">
      <a class="read-btn" href="#">Continue Reading</a>
      <span class="stat"><svg width="20" height="14" viewBox="0 0 20 14"><path d="M1 7 Q10 -3 19 7 Q10 17 1 7Z" fill="#333"/><circle cx="10" cy="7" r="3" fill="#fff"/></svg>56,681 views</span>
      <span class="stat"><svg width="16" height="16" viewBox="0 0 16 16"><rect x="1" y="7" width="3" height="8" fill="#333"/><path d="M5 7 L8 1 Q10 1 10 4 L10 6 L15 6 L14 15 L5 15Z" fill="#333"/></svg>525 Likes</span>
      <span class="stat"><svg width="16" height="16" viewBox="0 0 16 16" style="transform:rotate(180deg)"><rect x="1" y="7" width="3" height="8" fill="#333"/><path d="M5 7 L8 1 Q10 1 10 4 L10 6 L15 6 L14 15 L5 15Z" fill="#333"/></svg>256 Dislikes</span>
      <div class="share"><span></span><span></span><span></span></div>
    </div>
    <div class="post-rule"></div>
    <p class="comment-label">Post comments here...</p>
    <div class="comment-field">Enter text...</div>
    <div class="post-end"></div>
  </article>

  <article class="post">
    <div class="post-media">
      <div class="post-photo photo-camp" role="img" aria-label="Hiker beside an orange tent in the hills at sunset"></div>
      <div class="play"><svg width="70" height="70" viewBox="0 0 70 70"><circle cx="35" cy="35" r="32" fill="rgba(0,0,0,.25)" stroke="#fff" stroke-width="4"/><path d="M28 22 L50 35 L28 48 Z" fill="#fff"/></svg></div>
    </div>
    <div class="post-head">
      <h3 class="post-title">Nemo enim ipsam voluptatem quia voluptas</h3>
      <span class="post-date"><svg width="12" height="12" viewBox="0 0 12 12"><rect x="1" y="2" width="10" height="9" fill="none" stroke="#e81f30" stroke-width="1.4"/><path d="M1 5h10M4 0.5v3M8 0.5v3" stroke="#e81f30" stroke-width="1.4"/></svg>January 21, 2017</span>
    </div>
    <p class="post-body">Sed ut perspiciatis unde omnis iste natus error sit voluptatem accusantium doloremque laudantium, totam rem aperiam, eaque ipsa quae ab illo inventore veritatis et quasi architecto beatae vitae dicta sunt explicabo. Nemo enim ipsam voluptatem quia voluptas sit aspernatur aut odit aut fugit.</p>
    <div class="post-actions">
      <a class="read-btn" href="#">Continue Reading</a>
      <span class="stat"><svg width="20" height="14" viewBox="0 0 20 14"><path d="M1 7 Q10 -3 19 7 Q10 17 1 7Z" fill="#333"/><circle cx="10" cy="7" r="3" fill="#fff"/></svg>56,681 views</span>
      <span class="stat"><svg width="16" height="16" viewBox="0 0 16 16"><rect x="1" y="7" width="3" height="8" fill="#333"/><path d="M5 7 L8 1 Q10 1 10 4 L10 6 L15 6 L14 15 L5 15Z" fill="#333"/></svg>525 Likes</span>
      <span class="stat"><svg width="16" height="16" viewBox="0 0 16 16" style="transform:rotate(180deg)"><rect x="1" y="7" width="3" height="8" fill="#333"/><path d="M5 7 L8 1 Q10 1 10 4 L10 6 L15 6 L14 15 L5 15Z" fill="#333"/></svg>256 Dislikes</span>
      <div class="share"><span></span><span></span><span></span></div>
    </div>
    <div class="post-rule"></div>
    <p class="comment-label">Post comments here...</p>
    <div class="comment-field">Enter text...</div>
    <div class="post-end"></div>
  </article>

  <nav class="pager">
    <a class="prev" href="#">&lt;&lt; Prev</a>
    <a class="current" href="#">1</a>
    <a href="#">2</a>
    <a href="#">3</a>
    <a href="#">4</a>
    <a class="next" href="#">Next &gt;&gt;</a>
  </nav>
</main>

<aside class="upnext">
  <div class="upnext-head"><h2 class="section-title">Upnext Videos</h2></div>

  <div class="clip">
    <div class="clip-media"><div class="clip-photo clip-1" role="img" aria-label="Couple sitting by a river at dusk"></div>
      <div class="play"><svg viewBox="0 0 70 70"><circle cx="35" cy="35" r="31" fill="rgba(0,0,0,.2)" stroke="#fff" stroke-width="5"/><path d="M28 22 L50 35 L28 48 Z" fill="#fff"/></svg></div></div>
    <p class="clip-text">Nemo enim ipsam voluptatem quia voluptas sit aspernatur aut odit aut fugit, sed quia.</p>
    <div class="clip-meta"><span class="m">&#9650; 525 Likes</span><span class="m">&#9660; 125 Likes</span><div class="share"><span></span><span></span><span></span></div></div>
  </div>

  <div class="clip">
    <div class="clip-media"><div class="clip-photo clip-2" role="img" aria-label="Friends lying in a circle on the grass"></div>
      <div class="play"><svg viewBox="0 0 70 70"><circle cx="35" cy="35" r="31" fill="rgba(0,0,0,.2)" stroke="#fff" stroke-width="5"/><path d="M28 22 L50 35 L28 48 Z" fill="#fff"/></svg></div></div>
    <p class="clip-text">Nemo enim ipsam voluptatem quia voluptas sit aspernatur aut odit aut fugit, sed quia.</p>
    <div class="clip-meta"><span class="m">&#9650; 525 Likes</span><span class="m">&#9660; 125 Likes</span><div class="share"><span></span><span></span><span></span></div></div>
  </div>

  <div class="clip">
    <div class="clip-media"><div class="clip-photo clip-3" role="img" aria-label="Wedding couple beside a white car"></div>
      <div class="play"><svg viewBox="0 0 70 70"><circle cx="35" cy="35" r="31" fill="rgba(0,0,0,.2)" stroke="#fff" stroke-width="5"/><path d="M28 22 L50 35 L28 48 Z" fill="#fff"/></svg></div></div>
    <p class="clip-text">Nemo enim ipsam voluptatem quia voluptas sit aspernatur aut odit aut fugit, sed quia.</p>
    <div class="clip-meta"><span class="m">&#9650; 525 Likes</span><span class="m">&#9660; 125 Likes</span><div class="share"><span></span><span></span><span></span></div></div>
  </div>

  <div class="clip">
    <div class="clip-media"><div class="clip-photo clip-4" role="img" aria-label="Woman sitting with a skateboard on a road"></div>
      <div class="play"><svg viewBox="0 0 70 70"><circle cx="35" cy="35" r="31" fill="rgba(0,0,0,.2)" stroke="#fff" stroke-width="5"/><path d="M28 22 L50 35 L28 48 Z" fill="#fff"/></svg></div></div>
    <p class="clip-text">Nemo enim ipsam voluptatem quia voluptas sit aspernatur aut odit aut fugit, sed quia.</p>
    <div class="clip-meta"><span class="m">&#9650; 525 Likes</span><span class="m">&#9660; 125 Likes</span><div class="share"><span></span><span></span><span></span></div></div>
  </div>

  <div class="clip">
    <div class="clip-media"><div class="clip-photo clip-5" role="img" aria-label="Person in a sunlit autumn field"></div>
      <div class="play"><svg viewBox="0 0 70 70"><circle cx="35" cy="35" r="31" fill="rgba(0,0,0,.2)" stroke="#fff" stroke-width="5"/><path d="M28 22 L50 35 L28 48 Z" fill="#fff"/></svg></div></div>
    <p class="clip-text">Nemo enim ipsam voluptatem quia voluptas sit aspernatur aut odit aut fugit, sed quia.</p>
    <div class="clip-meta"><span class="m">&#9650; 525 Likes</span><span class="m">&#9660; 125 Likes</span><div class="share"><span></span><span></span><span></span></div></div>
  </div>
</aside>

<footer class="site-footer">
  <div class="footer-brand"><span class="brand-mark"></span>KOVE CLIPS</div>
  <nav class="footer-nav">
    <a href="#">HOME</a><span class="sep">|</span>
    <a href="#">ABOUT</a><span class="sep">|</span>
    <a href="#">UPLOAD VIDEOS</a><span class="sep">|</span>
    <a href="#">NEWS</a><span class="sep">|</span>
    <a href="#">PORTFOLIO</a><span class="sep">|</span>
    <a href="#">CONTACT US</a>
  </nav>
  <div class="footer-rule"></div>
  <p class="copyright">© 2017 Kove Clips. All Rights Reserved</p>
  <div class="footer-social"><span></span><span></span><span></span><span></span><span></span></div>
</footer>

</body>
</html>
```